Warren D Pellham New Business Card Design

I assist families or individuals with downsizing. When they need to sell estate items I manage the process. I may buy their items. I may place their items with auction houses or I may bring in a variety of experts to sell all of the items. We help clients sell a huge variety of items including art, jewelry, coins, watches, antiques, collectibles, etc.

Target Market(s)

Two markets...One market is the clients I serve which are usually seniors or their family. These are individuals that need to sell on item or a house full if they estate is being liquidated. The other market is those that refer clients to me. Real Estate professionals, active senior communities, trust and estate lawyers and financial advisors.

Contact Information for Business Card

This is a new business so we do not have a logo. We may not need a logo. Feel free to visit our website at www.warrendpellham-example.com for more information on the service we provide. I am a private consultant so my name needs to be prominent. My name is my brand. We need the card to let people know how to contact us via phone, website and email. Easy to read. Many of our clients are elderly.

Font styles to use
Sans Serif

Requirements
Must have
• My name. Our contact information.
• Warren D Pellham
• 555-218-7034 Office
• 555-639-1582 Cell
• info@warrendpellham-example.com
• www.warrendpellham-example.com

```html
<!DOCTYPE html>
<html lang="en">
<head>
<meta charset="utf-8">
<title>Warren D Pellham – Business Card</title>
<link href="https://fonts.googleapis.com/css2?family=Raleway:wght@400;500;800&display=swap" rel="stylesheet">
<style>
  :root {
    --page-bg: #e9ecef;
    --card-white: #ffffff;
    --ink-blue: #0f5d86;
    --icon-blue: #0d5a83;
    --text-dark: #1f2a33;
    --photo-light: #e4f3fb;
    --photo-mid: #a9d4ec;
    --wave-deep: #0a5f95;
    --wave-mid: #3d9bd3;
    --wave-light: #9fd0ee;
  }
  html, body {
    margin: 0;
    padding: 0;
    width: 1200px;
    height: 900px;
    overflow: hidden;
    background: var(--page-bg);
    font-family: "Raleway", Arial, sans-serif;
  }
  .business-card {
    position: absolute;
    left: 100px;
    top: 164px;
    width: 1000px;
    height: 572px;
    background: var(--card-white);
    box-shadow: 0 10px 30px rgba(0,0,0,0.18);
    overflow: hidden;
  }
  .portrait-area {
    position: absolute;
    left: 0;
    top: 0;
    width: 470px;
    height: 572px;
    background: linear-gradient(160deg, var(--photo-light) 0%, #cfe8f6 55%, var(--photo-mid) 100%);
  }
  .wave-divider {
    position: absolute;
    left: 0;
    top: 0;
    width: 1000px;
    height: 572px;
  }
  .card-name {
    position: absolute;
    left: 486px;
    top: 170px;
    margin: 0;
    font-size: 42px;
    font-weight: 400;
    color: var(--ink-blue);
    white-space: nowrap;
    letter-spacing: 0.2px;
  }
  .card-name .surname {
    font-weight: 800;
  }
  .contact-list {
    position: absolute;
    left: 506px;
    top: 316px;
    margin: 0;
    padding: 0;
    list-style: none;
  }
  .contact-item {
    display: flex;
    align-items: center;
    height: 38px;
    font-size: 24px;
    font-weight: 500;
    color: var(--text-dark);
    white-space: nowrap;
  }
  .contact-icon {
    width: 26px;
    height: 26px;
    margin-right: 12px;
    flex: none;
  }
</style>
</head>
<body>
  <div class="business-card">
    <div class="portrait-area" role="img" aria-label="Portrait photo of Warren D Pellham in a dark suit, arms crossed, on a light blue backdrop"></div>

    <svg class="wave-divider" viewBox="0 0 1000 572" aria-hidden="true">
      <path d="M400 0 C 330 130, 450 320, 395 572 L 470 572 L 470 0 Z" fill="var(--wave-light)"/>
      <path d="M420 0 C 350 130, 470 320, 415 572 L 470 572 L 470 0 Z" fill="var(--wave-mid)"/>
      <path d="M432 0 C 362 130, 482 320, 427 572" fill="none" stroke="#ffffff" stroke-width="3"/>
      <path d="M444 0 C 374 130, 494 320, 439 572" fill="none" stroke="var(--wave-deep)" stroke-width="6"/>
      <path d="M452 0 C 382 130, 502 320, 447 572 L 1000 572 L 1000 0 Z" fill="var(--card-white)"/>
    </svg>

    <h1 class="card-name">Warren D. <span class="surname">PELLHAM</span></h1>

    <ul class="contact-list">
      <li class="contact-item">
        <svg class="contact-icon" viewBox="0 0 28 28" aria-hidden="true">
          <circle cx="14" cy="14" r="14" fill="var(--icon-blue)"/>
          <path d="M9 7.5 l3 -0.5 l1.5 4 l-2 1.5 c1 2 2.5 3.5 4.5 4.5 l1.5 -2 l4 1.5 l-0.5 3 c-7 1 -13 -5 -12 -12z" fill="#fff"/>
        </svg>
        555-218-7034
      </li>
      <li class="contact-item">
        <svg class="contact-icon" viewBox="0 0 28 28" aria-hidden="true">
          <circle cx="14" cy="14" r="14" fill="var(--icon-blue)"/>
          <rect x="9.5" y="6.5" width="9" height="15" rx="1.8" fill="none" stroke="#fff" stroke-width="2"/>
          <circle cx="14" cy="18.5" r="1" fill="#fff"/>
        </svg>
        555-639-1582
      </li>
      <li class="contact-item">
        <svg class="contact-icon" viewBox="0 0 28 28" aria-hidden="true">
          <circle cx="14" cy="14" r="14" fill="var(--icon-blue)"/>
          <rect x="7" y="9" width="14" height="10" rx="1" fill="#fff"/>
          <path d="M7.5 9.5 L14 14.5 L20.5 9.5" fill="none" stroke="var(--icon-blue)" stroke-width="1.5"/>
        </svg>
        info@warrendpellham-example.com
      </li>
      <li class="contact-item">
        <svg class="contact-icon" viewBox="0 0 28 28" aria-hidden="true">
          <circle cx="14" cy="14" r="14" fill="var(--icon-blue)"/>
          <circle cx="14" cy="14" r="8" fill="none" stroke="#fff" stroke-width="1.8"/>
          <ellipse cx="14" cy="14" rx="3.5" ry="8" fill="none" stroke="#fff" stroke-width="1.5"/>
          <line x1="6" y1="14" x2="22" y2="14" stroke="#fff" stroke-width="1.5"/>
        </svg>
        www.warrendpellham-example.com
      </li>
    </ul>
  </div>
</body>
</html>
```